Excellent Rewards: Escort Services for Men needs Banner Ad Design

We need a banner ad design for a company based in Brazil called "Lunaré" (http://www.lunare-app.com.br), which offers escort services for men. Our main strength and focus is helping people easily search for escorts using mobile devices, by being an mobile optimized repository of escorts which are crawled from many non-mobile optimized sites.

Target Market(s)

Men at all ages (above 18) looking for escorts

Industry/Entity Type

Escort

Requirements
Must have
• Size must be 468x60
The logo must be on white background
Nice to have
• The banner could have an eye-catching animation

The banner could have a small and quick animation showing the usage of the mobile application (like navigating through the application).
Should not have
• If animated then the text should not be split between frames.

```html
<!DOCTYPE html>
<html lang="pt-BR">
<head>
<meta charset="utf-8">
<title>Lunaré — Banner 468x60</title>
<link rel="stylesheet" href="https://fonts.googleapis.com/css2?family=Open+Sans:wght@400;700&display=swap">
<style>
  :root {
    --backdrop-center: #6a6a6a;
    --backdrop-edge: #262626;
    --banner-bg: #ffffff;
    --brand-red: #8e1a22;
    --copy-grey: #6b6b6b;
    --device-dark: #1c1c1c;
    --screen-warm: #c99a7e;
    --screen-cool: #7fb3c2;
  }
  * { margin: 0; padding: 0; box-sizing: border-box; }
  html, body { width: 1200px; height: 900px; overflow: hidden; }
  body {
    background: radial-gradient(ellipse 60% 60% at 50% 50%, var(--backdrop-center), var(--backdrop-edge));
    font-family: "Open Sans", Helvetica, Arial, sans-serif;
    position: relative;
  }
  .banner {
    position: absolute;
    left: 132px; top: 390px;
    width: 936px; height: 120px;
    background: var(--banner-bg);
  }
  .brand {
    position: absolute;
    left: 16px; top: 0; height: 120px;
    display: flex; align-items: center; gap: 10px;
  }
  .brand-dot {
    width: 26px; height: 26px; border-radius: 50%;
    background: var(--brand-red);
  }
  .brand-name {
    font-weight: 700; font-size: 40px;
    color: var(--brand-red);
    letter-spacing: -0.5px;
  }
  .tagline {
    position: absolute;
    left: 230px; width: 436px; top: 12px;
    text-align: center;
    font-size: 28px; line-height: 32px; font-weight: 400;
    color: var(--copy-grey);
  }
  .device {
    position: absolute;
    left: 680px; top: 6px;
    width: 226px; height: 106px;
    border-radius: 12px;
    background: var(--device-dark);
    padding: 8px 28px;
  }
  .device-screen {
    width: 100%; height: 100%;
    background: linear-gradient(110deg, var(--screen-warm) 0%, #e7c7ad 45%, var(--screen-cool) 100%);
  }
</style>
</head>
<body>
  <div class="banner">
    <div class="brand">
      <span class="brand-dot"></span>
      <span class="brand-name">Lunaré</span>
    </div>
    <p class="tagline">O maior catálogo de<br>acompanhantes na palma<br>da sua mão</p>
    <div class="device">
      <div class="device-screen" role="img" aria-label="Foto de uma modelo reclinada exibida na tela de um smartphone"></div>
    </div>
  </div>
</body>
</html>
```